Create a Graphic About YOURSELF and PixelHarbor

PixelHarbor would like you (designers) to create an awesome graphic to promote YOURSELF and your profile on PixelHarbor!

Your graphic should communicate your name, your services and should mention PixelHarbor.

The design should be perfect for sharing on Chatterly. Here's an example of what we'd like http://blog.pixelharbor-example.ca/article/333/pixelharbor-launches-3000-hire-me-social-design-contest

Once you submitted your design, we'd love you to share the design ('advertisement') and promote yourself and PixelHarbor to your friends and potential customers. So make your submissions great and get your friends to vote for your design by 'Liking' it on Chatterly!

Prizes:
$1500 - "PixelHarbor Community" prize awarded to the designer with the most Chatterly 'Likes'
5 x $50 for the next 5 'most liked' designs on Chatterly

$1000 - "Hire Me" prize awarded to the designer who receives the most client invites
5 x $50 for the next 5 'most invited' designers

In summary, this is a great opportunity for you to increase your exposure to PixelHarbor customers and win cash prizes. Show off your design skills and get hired by PixelHarbor customers from around the world!

Target Market(s)

Fans, friends and customers of YOU

Industry/Entity Type

Cash

Requirements
Must have
• 1) Include your PixelHarbor user name on the graphic so customers can find you in the PixelHarbor Designer Directory
2) Include the tagline "Hire Me on PixelHarbor.com!" in your graphic design.
3) Share your design's URL on our Chatterly wall at http://chatterly-example.com/pixelharbor and get your friends to 'like' your design.
Nice to have
• 1) Include a tagline that expresses your design approach/philosophy
2) Artwork dimensions: 403 x 403 px
3) You can submit more than 1 design!
Should not have
• You must own the copyright of any images you use including stock imagery.

```html
<!DOCTYPE html>
<html lang="en">
<head>
<meta charset="utf-8">
<title>Noreen Talwar — Hire Me on PixelHarbor.com!</title>
<link href="https://fonts.googleapis.com/css2?family=Quicksand:wght@400;600;700&family=Titan+One&display=swap" rel="stylesheet">
<style>
  :root {
    --bg-core: #f53a05;
    --bg-mid: #c41d02;
    --bg-edge: #7e0800;
    --band: #000000;
    --service: #ffffff;
    --name: #ffe400;
    --accent: #ffe400;
    --platform: #ffffff;
  }
  html, body {
    margin: 0;
    padding: 0;
    width: 1200px;
    height: 900px;
    overflow: hidden;
    background: var(--bg-edge);
  }
  .promo {
    display: block;
    width: 1200px;
    height: 900px;
  }
  .service {
    font-family: "Quicksand", sans-serif;
    font-weight: 400;
    font-size: 50px;
    fill: var(--service);
    filter: drop-shadow(3px 4px 3px rgba(0,0,0,0.55));
  }
  .service .strong { font-weight: 700; }
  .name {
    font-family: "Quicksand", sans-serif;
    font-weight: 400;
    font-size: 66px;
    fill: var(--name);
    filter: drop-shadow(3px 4px 3px rgba(0,0,0,0.6));
  }
  .name .strong { font-weight: 700; }
  .band { fill: var(--band); }
  .hire-line {
    font-family: "Titan One", sans-serif;
    font-size: 30px;
    fill: var(--accent);
    filter: drop-shadow(2px 2px 1px rgba(0,0,0,0.6));
  }
  .platform-name {
    font-family: "Quicksand", sans-serif;
    font-weight: 700;
    font-size: 40px;
    fill: var(--platform);
  }
</style>
</head>
<body>
<svg class="promo" viewBox="0 0 1200 900" xmlns="http://www.w3.org/2000/svg">
  <defs>
    <radialGradient id="backdrop" cx="430" cy="400" r="900" gradientUnits="userSpaceOnUse">
      <stop offset="0" stop-color="#f53a05"/>
      <stop offset="0.45" stop-color="#c41d02"/>
      <stop offset="1" stop-color="#7e0800"/>
    </radialGradient>
  </defs>

  <rect class="backdrop" width="1200" height="900" fill="url(#backdrop)"/>

  <g class="services">
    <text class="service" transform="translate(402 432) rotate(-52.4)" textLength="365" lengthAdjust="spacingAndGlyphs">web design</text>
    <text class="service" transform="translate(470 478) rotate(-45.6)" textLength="460" lengthAdjust="spacingAndGlyphs">graphic design</text>
    <text class="service" transform="translate(515 522) rotate(-38.7)" textLength="390" lengthAdjust="spacingAndGlyphs"><tspan class="strong">2</tspan>d animation</text>
    <text class="service" transform="translate(545 560) rotate(-29)" textLength="415" lengthAdjust="spacingAndGlyphs">photography</text>
    <text class="service" transform="translate(560 618) rotate(-18)" textLength="285" lengthAdjust="spacingAndGlyphs">digital art</text>
    <text class="service" transform="translate(580 690) rotate(-13.5)" textLength="220" lengthAdjust="spacingAndGlyphs">fine art</text>
  </g>

  <polygon class="band" points="255,560 413,738 195,900 0,900 0,790"/>
  <g class="designer-name">
    <text class="name" transform="translate(160 740) rotate(-41)" textLength="350" lengthAdjust="spacingAndGlyphs">nor<tspan class="strong">een</tspan></text>
    <text class="name" transform="translate(228 795) rotate(-42.4)" textLength="330" lengthAdjust="spacingAndGlyphs">talwar</text>
  </g>

  <g class="hire-tag">
    <text class="hire-line" transform="translate(918 822) rotate(-32)" textLength="250" lengthAdjust="spacingAndGlyphs">HIRE ME ON</text>
    <text class="platform-name" transform="translate(940 878) rotate(-28)" textLength="300" lengthAdjust="spacingAndGlyphs">PixelHarbor.com</text>
  </g>
</svg>
</body>
</html>
```